The Greenvale Open for Pitch Stars™

Please go to www.greenvaleopenstars.com and if you are a professional web designer you know what needs to be done!
I need a fresh, modern but still 'credible' design (authority!) - after all the event is an official World Championship!
Content (text, pics etc.) remains the same.
A new, trademarked logo has been developed and needs to be used throughout the site.
The site must include the possibility to be able to update/change content by ourselfs using a simple CMS.
Project duration: 5 days or less.
Main reason being for such a short period of time: we are AT PRESENT in negociations with all kinds of stakeholders and would like to impress them ASAP!
Could be an ongoing job for next couple of months.
Key words: official World Championship, golf, football, first sports cross over event ever, authority, fun, BRAZIL (hosting country), excitement, television, country's honour, another Global Trophy, PASSION!!
Pictures on website can be used - our/my responsibility.
Good luck!

Target Market(s)

(ex) Footballers - european soccer.
Golfers
People interested in sports

Industry/Entity Type

Event

Requirements
Must have
• Golf
Football
Brazil
Authority
World Championship

```html
<!DOCTYPE html>
<html lang="en">
<head>
<meta charset="utf-8">
<title>The Greenvale Open for Pitch Stars™ 2014</title>
<link href="https://fonts.googleapis.com/css2?family=Bebas+Neue&family=Arimo:wght@400;700&display=swap" rel="stylesheet">
<style>
:root{
  --green-deep:#033222;
  --green-dark:#0a4a33;
  --green-mid:#1d7a45;
  --green-bright:#4fae3a;
  --green-pale:#e6f3df;
  --lime:#c9dc7a;
  --gold:#b5983f;
  --ink:#1b3a2c;
  --white:#ffffff;
  --title:#0f4a36;
}
*{margin:0;padding:0;box-sizing:border-box}
html,body{width:1045px;height:1200px;overflow:hidden}
body{
  position:relative;
  font-family:"Arimo",Arial,sans-serif;
  background:
    linear-gradient(90deg,rgba(10,60,25,.35) 0,rgba(10,60,25,0) 110px,rgba(10,60,25,0) 935px,rgba(10,60,25,.35) 1045px),
    linear-gradient(180deg,#ffffff 0,#eef7e8 70px,#c4dd96 160px,#7fb652 290px,#4e9a3f 430px,#4f9d45 560px,#b8ddb0 680px,#ffffff 760px,#ffffff 965px,#d3e9cb 1010px,#1d7a45 1032px);
}
.swoosh{position:absolute;left:0;top:0;width:1045px;height:1040px}

.brand{position:absolute;left:0;top:10px;width:1045px;text-align:center}
.brand-mark{display:inline-block;width:56px;height:56px;border-radius:50%;background:var(--gold)}
.brand-name{font-family:"Bebas Neue",sans-serif;color:var(--gold);font-size:14px;letter-spacing:1.5px;margin-top:10px;line-height:1.05}

.main-nav{position:absolute;left:108px;top:119px;width:832px;height:52px;display:flex;border-radius:8px;
  background:linear-gradient(180deg,#0b5a3e 0,#034026 60%,#03301d 100%);box-shadow:0 3px 6px rgba(0,0,0,.3)}
.main-nav a{position:relative;display:flex;align-items:center;justify-content:center;color:var(--white);text-decoration:none;
  font-family:"Bebas Neue",sans-serif;font-size:16px;letter-spacing:.3px;border-right:1px solid rgba(255,255,255,.12)}
.main-nav a:last-child{border-right:0}
.main-nav a.active::before{content:"";position:absolute;left:19px;right:14px;top:10px;bottom:10px;border-radius:8px 8px 2px 2px;
  background:linear-gradient(180deg,#7fb9a2 0,#2d7c5e 35%,#0c5a3f 100%)}
.main-nav a span{position:relative;z-index:1}

.hero{position:absolute;left:110px;top:190px;width:828px;height:253px;border-radius:8px;overflow:hidden;border:2px solid #b9e1a9;
  background:linear-gradient(180deg,#25621c 0,#2f7424 45%,#3d8a2c 75%,#2a6a1f 100%)}
.hero-text{position:absolute;left:25px;top:46px;color:var(--white);font-family:"Bebas Neue",sans-serif}
.hero-kicker{font-size:21px;letter-spacing:.2px}
.hero-date{font-size:57px;line-height:52px;margin-top:8px;text-shadow:0 2px 4px rgba(0,0,0,.5)}

.feature{position:absolute;top:475px;width:257px;height:175px}
.feature-tab{height:29px;border-radius:7px 7px 0 0;background:linear-gradient(180deg,#1f8460 0,#07462f 100%);
  color:var(--white);font-family:"Bebas Neue",sans-serif;font-size:14.5px;text-align:center;line-height:31px}
.feature-photo{height:142px;border:4px solid #e4f6dc;border-radius:0 0 7px 7px}
.feature-more{position:absolute;right:18px;bottom:0;width:66px;height:27px;border-radius:8px;
  background:linear-gradient(180deg,#1d6a4f 0,#04382a 100%);color:var(--white);font-size:10px;text-align:center;line-height:27px}
.photo-golfer{background:linear-gradient(180deg,#6f8f52 0,#86a466 55%,#b9cf94 100%)}
.photo-course{background:linear-gradient(180deg,#cfe2ee 0,#5f8d45 35%,#7fae57 100%)}
.photo-trophy{background:linear-gradient(180deg,#fafbd2 0,#f2f5b8 100%)}

.intro{position:absolute;left:122px;top:690px;width:535px;color:var(--ink)}
.intro-title{font-family:"Bebas Neue",sans-serif;color:var(--title);font-size:22px;font-weight:400;padding-left:2px;
  padding-bottom:8px;border-bottom:1px solid #e1ece0;width:330px}
.intro p{font-size:10px;line-height:12px;margin-top:27px}
.intro p + p{margin-top:40px}

.roster{position:absolute;left:124px;top:902px;display:flex;gap:6px}
.player{width:59px;text-align:center;font-size:9px;color:var(--ink);line-height:11px}
.player-photo{width:59px;height:56px;border:1px solid #d9c98e;margin-bottom:12px}
.tone-a{background:linear-gradient(180deg,#4f6c5a 0,#2a3f36 100%)}
.tone-b{background:linear-gradient(180deg,#7c98b3 0,#3e5670 100%)}
.tone-c{background:linear-gradient(180deg,#6f8e4f 0,#2e3b2a 100%)}
.tone-d{background:linear-gradient(180deg,#8a8f86 0,#3c3f3a 100%)}
.tone-e{background:linear-gradient(180deg,#e9efe0 0,#6d9a6a 100%)}
.tone-f{background:linear-gradient(180deg,#f2ecb0 0,#c95a4a 100%)}
.tone-g{background:linear-gradient(180deg,#9fb98a 0,#5f7d4e 100%)}
.tone-h{background:linear-gradient(180deg,#4e6870 0,#1f2a30 100%)}
.player b{display:block;font-size:9.5px;color:var(--green-dark)}

.contact{position:absolute;left:722px;top:707px;width:205px}
.contact-tab{height:32px;border-radius:7px 7px 0 0;background:linear-gradient(180deg,#1f8460 0,#07462f 100%);
  color:var(--white);font-family:"Bebas Neue",sans-serif;font-size:15px;line-height:34px;padding-left:17px}
.contact-panel{margin:0 2px;padding:10px 15px 12px;background:linear-gradient(180deg,#0d5a40 0,#06412c 60%,#032a1c 100%);
  border-radius:6px;border-top:1px solid #2a7d5c;color:#d7eadf;font-size:9px;line-height:11px}
.contact-panel h3{font-size:10.5px;color:#6fcf8a;text-decoration:underline;letter-spacing:.6px;margin-bottom:12px}
.social{display:flex;gap:3px}
.social span{width:18px;height:18px;border-radius:3px;background:#7fbf9a}
.panel-follow{height:79px}
.panel-phone{height:73px}
.panel-address{height:90px}

.footer{position:absolute;left:0;top:1032px;width:1045px;height:168px;background:var(--green-deep)}
.footer-nav{position:absolute;top:45px;left:0;width:1045px;height:20px}
.footer-nav a{position:absolute;color:var(--white);text-decoration:none;font-family:"Bebas Neue",sans-serif;font-size:15px}
.copyright{position:absolute;top:92px;width:1045px;text-align:center;color:var(--white);font-family:"Bebas Neue",sans-serif;font-size:14px}
</style>
</head>
<body>

<svg class="swoosh" viewBox="0 0 1045 1040" aria-hidden="true">
  <path d="M0 85 Q520 150 1045 85 L1045 130 Q520 200 0 130Z" fill="#1f7a3c" opacity=".8"/>
  <path d="M0 125 Q520 185 1045 125 L1045 150 Q520 205 0 150Z" fill="#dfe98c" opacity=".6"/>
  <path d="M0 570 Q520 520 1045 570 L1045 620 Q520 575 0 620Z" fill="#1a6e33" opacity=".55"/>
  <path d="M0 560 Q200 550 250 560 L0 580Z" fill="#ffffff" opacity=".4"/>
  <path d="M1045 560 Q850 550 800 560 L1045 580Z" fill="#ffffff" opacity=".4"/>
</svg>

<header class="brand">
  <span class="brand-mark"></span>
  <div class="brand-name">The Greenvale Open for Pitch Stars™<br>2014</div>
</header>

<nav class="main-nav">
  <a class="active" style="width:106px"><span>Home</span></a>
  <a style="width:57px"><span>Event</span></a>
  <a style="width:73px"><span>Venue</span></a>
  <a style="width:82px"><span>Teams</span></a>
  <a style="width:98px"><span>Ambassadors</span></a>
  <a style="width:107px"><span>Endorsements</span></a>
  <a style="width:62px"><span>News</span></a>
  <a style="width:64px"><span>Media</span></a>
  <a style="width:83px"><span>About Us</span></a>
  <a style="width:100px"><span>Contact Us</span></a>
</nav>

<section class="hero" role="img" aria-label="Close-up of a golf ball resting on green grass">
  <div class="hero-text">
    <div class="hero-kicker">THE GREENVALE OPEN FOR PITCH STARS™</div>
    <div class="hero-date">JUNE 5-8, 2014,<br>RIO DE JANEIRO, BRAZIL</div>
  </div>
</section>

<article class="feature" style="left:120px">
  <div class="feature-tab">The best golfing footballers 2014</div>
  <div class="feature-photo photo-golfer" role="img" aria-label="Footballer swinging a golf club on a course"></div>
  <a class="feature-more">MORE</a>
</article>
<article class="feature" style="left:396px">
  <div class="feature-tab">The world's most challenging golf courses</div>
  <div class="feature-photo photo-course" role="img" aria-label="Golf course with palm trees and bunkers"></div>
  <a class="feature-more">MORE</a>
</article>
<article class="feature" style="left:671px">
  <div class="feature-tab">The Global Trophy's 2014 media coverage</div>
  <div class="feature-photo photo-trophy" role="img" aria-label="Global Trophy 2014 emblem"></div>
  <a class="feature-more">MORE</a>
</article>

<section class="intro">
  <h1 class="intro-title">The Greenvale Open for Pitch Stars™</h1>
  <p>One doesn't need to be a fanatical supporter of either golf or football to get a sense of just how much interest and excitement the Greenvale Open for Pitch Stars© will generate: an A-list of current and former players and coaches from the world's most popular spectator sport, playing the world's fastest growing participation sport, on the world's most beautiful golf courses, just has to be a winner!</p>
  <p>"These guys have performed in front of millions of people on a weekly basis. It will be fascinating to see how they hold their nerves outside their comfort zones but still in a very competitive environment..."</p>
</section>

<section class="roster">
  <div class="player"><div class="player-photo tone-a" role="img" aria-label="Player portrait"></div>Ivo<b>Wrenfield</b></div>
  <div class="player"><div class="player-photo tone-b" role="img" aria-label="Player portrait"></div>Frans<b>Rijvelt</b></div>
  <div class="player"><div class="player-photo tone-c" role="img" aria-label="Player portrait"></div>Piet<b>Schonmark</b></div>
  <div class="player"><div class="player-photo tone-d" role="img" aria-label="Player portrait"></div>Alden<b>Sherwood</b></div>
  <div class="player"><div class="player-photo tone-e" role="img" aria-label="Player portrait"></div>Olaf<b>Kessing</b></div>
  <div class="player"><div class="player-photo tone-f" role="img" aria-label="Player portrait"></div>Lauro<b>Fideles</b></div>
  <div class="player"><div class="player-photo tone-g" role="img" aria-label="Player portrait"></div>Pau<b>Garrido</b></div>
  <div class="player"><div class="player-photo tone-h" role="img" aria-label="Player portrait"></div>Floris<b>De Berg</b></div>
</section>

<aside class="contact">
  <div class="contact-tab">Contact Us</div>
  <div class="contact-panel panel-follow">
    <h3>Follow Us</h3>
    <div class="social" aria-label="Social network links"><span></span><span></span><span></span><span></span><span></span></div>
  </div>
  <div class="contact-panel panel-phone">
    <h3>Phone Numbers</h3>
    + 34 600 111 234<br>+ 34 900 555 018
  </div>
  <div class="contact-panel panel-address">
    <h3>Address</h3>
    GVO - Events Lda<br>Rua das Palmeiras 12<br>9000 - 100 Vilaverde<br>Ilha Verde - Portugal
  </div>
</aside>

<footer class="footer">
  <nav class="footer-nav">
    <a style="left:132px">Home</a>
    <a style="left:211px">Event</a>
    <a style="left:276px">Venue</a>
    <a style="left:351px">Teams</a>
    <a style="left:424px">Ambassadors</a>
    <a style="left:527px">Endorsements</a>
    <a style="left:632px">News</a>
    <a style="left:697px">Media</a>
    <a style="left:762px">About Us</a>
    <a style="left:840px">Contact Us</a>
  </nav>
  <div class="copyright">© GVO Events Lda. All rights reserved.</div>
</footer>

</body>
</html>
```